Book jacket for Drumlore

We need a book jacket design (hard cover front, back, spine, flaps; soft cover and eBook). for a social psychology book with the general cluelessness (being "out of it") of how people function both in their personal and social lives. This is the third book written by the author, a practicing psychiatrist, and the content centers on a single subject, people's lack of genuine emotional contact, their cluelessness with themselves and with current national and world events.

Target Market(s)

People who want to better understand the state the nation and world is in now, and what they can do about it.

Font styles to use
Serif
Sans Serif

Requirements
Must have
• Bold, eye-catching cover
Nice to have
• Like the idea of separating the title word (drum lore) to better emphasize the concept of lack of contact

```html
<!DOCTYPE html>
<html lang="en">
<head>
<meta charset="utf-8">
<title>Drumlore — Book Cover</title>
<link rel="stylesheet" href="https://fonts.googleapis.com/css2?family=Montserrat:wght@800;900&family=Kaushan+Script&display=swap">
<style>
  :root {
    --cover-red: #ae1e15;
    --ink-black: #000000;
    --paper-white: #ffffff;
  }
  html, body {
    margin: 0;
    padding: 0;
    width: 800px;
    height: 1200px;
    overflow: hidden;
    background: var(--cover-red);
  }
  .book-cover {
    position: relative;
    width: 800px;
    height: 1200px;
    background: var(--cover-red);
    overflow: hidden;
  }
  .title {
    margin: 0;
    font-weight: normal;
  }
  .title-word-primary {
    position: absolute;
    left: 0;
    right: 0;
    top: 175px;
    text-align: center;
    font-family: "Montserrat", sans-serif;
    font-weight: 900;
    font-size: 222px;
    line-height: 1;
    letter-spacing: -6px;
    color: var(--ink-black);
  }
  .title-word-secondary {
    position: absolute;
    left: 100px;
    top: 268px;
    font-family: "Kaushan Script", cursive;
    font-size: 250px;
    line-height: 1;
    letter-spacing: 2px;
    color: var(--paper-white);
    transform: rotate(-4deg);
    transform-origin: left bottom;
  }
  .author {
    position: absolute;
    left: 0;
    right: 0;
    top: 1109px;
    margin: 0;
    text-align: center;
    font-family: "Montserrat", sans-serif;
    font-weight: 800;
    font-size: 50px;
    line-height: 1;
    letter-spacing: 0.5px;
    color: var(--paper-white);
  }
</style>
</head>
<body>
  <main class="book-cover">
    <h1 class="title" aria-label="Drumlore">
      <span class="title-word-primary">DRUM</span>
      <span class="title-word-secondary">LORE</span>
    </h1>
    <p class="author">MARTIN HOLLAS M.D.</p>
  </main>
</body>
</html>
```